Google Doc: Online Personal Training New Client Onboarding form

I would like you to create a google doc for online training following this format but matching my style and logo and branding/colours. My style is black/grey/red/white not pink

```html
<!DOCTYPE html>
<html lang="en">
<head>
<meta charset="utf-8">
<title>Online Personal Training New Client Onboarding Form</title>
<link href="https://fonts.googleapis.com/css2?family=Lobster&family=Roboto:ital,wght@0,400;0,500;0,700;1,400&display=swap" rel="stylesheet">
<style>
  :root {
    --page-bg: #f0f0f0;
    --card-bg: #ffffff;
    --card-border: #dadce0;
    --banner-bg: #eeeeee;
    --brand-grey: #58595b;
    --accent-bar: #58595b;
    --text-main: #202124;
    --text-muted: #5f6368;
    --link-blue: #1a73e8;
    --required-red: #d93025;
    --line: #dadce0;
  }
  * { box-sizing: border-box; margin: 0; padding: 0; }
  html, body {
    width: 1200px; height: 749px; overflow: hidden;
    background: var(--page-bg);
    font-family: "Roboto", Arial, sans-serif;
    color: var(--text-main);
  }
  body { position: relative; }
  .form-column {
    position: absolute; left: 333px; top: 53px; width: 534px;
    height: 696px; overflow: hidden;
  }
  .brand-banner {
    height: 133px; background: var(--banner-bg);
    border: 1px solid var(--card-border); border-radius: 8px;
    display: flex; align-items: center; justify-content: center; gap: 12px;
  }
  .brand-square { width: 22px; height: 22px; background: var(--brand-grey); }
  .brand-name {
    font-family: "Roboto", Arial, sans-serif; font-weight: 500;
    color: var(--brand-grey); font-size: 24px; line-height: 1;
  }
  .card {
    background: var(--card-bg); border: 1px solid var(--card-border);
    border-radius: 8px; margin-top: 12px;
  }
  .intro-card { border-top: 8px solid var(--accent-bar); margin-top: 13px; }
  .intro-body { padding: 13px 21px 10px; }
  .form-title {
    font-family: "Lobster", cursive; font-weight: 400;
    font-size: 25px; line-height: 29px; letter-spacing: -0.2px; color: var(--text-main);
  }
  .form-lead { font-size: 14px; margin-top: 4px; line-height: 20px; }
  .form-motto { font-size: 14px; font-style: italic; margin-top: 18px; line-height: 19px; }
  .account-row {
    border-top: 1px solid var(--line); padding: 9px 21px 0;
    display: flex; align-items: center; font-size: 13px; color: var(--text-muted);
    height: 29px; box-sizing: content-box;
  }
  .account-row .email { font-weight: 500; margin-left: 10px; }
  .account-row .switch { color: var(--link-blue); margin-left: 4px; }
  .account-row .cloud { margin-left: auto; }
  .required-note { color: var(--required-red); font-size: 13px; line-height: 16px; padding: 2px 21px 15px; }
  .question-card { height: 112px; padding: 19px 21px; }
  .question-label { font-size: 14px; line-height: 18px; font-weight: 700; }
  .question-label .star { color: var(--required-red); font-weight: 400; }
  .answer-line {
    margin-top: 27px; width: 244px; font-size: 13px; line-height: 16px; color: var(--text-muted);
    border-bottom: 1px solid var(--line); padding-bottom: 5px;
  }
  .report-icon { position: absolute; left: 11px; top: 716px; }
  .edit-button {
    position: absolute; left: 1139px; top: 688px; width: 41px; height: 41px;
    border-radius: 50%; background: var(--card-bg);
    box-shadow: 0 1px 4px rgba(0,0,0,0.25);
    display: flex; align-items: center; justify-content: center;
  }
</style>
</head>
<body>
  <main class="form-column">
    <header class="brand-banner">
      <span class="brand-square"></span>
      <span class="brand-name">Marco Velden Personal Training</span>
    </header>

    <section class="card intro-card">
      <div class="intro-body">
        <h1 class="form-title">Online Personal Training New Client Onboarding Form</h1>
        <p class="form-lead">Please fill out this application form if you are ready to be part of my team.</p>
        <p class="form-motto">Time to level up you to make accountable for yourself and help you achieve your fitness goals!</p>
      </div>
      <div class="account-row">
        <svg width="20" height="18" viewBox="0 0 24 20" fill="none" stroke="#5f6368" stroke-width="2">
          <path d="M2 10c3-5 7-7 10-7s7 2 10 7c-3 5-7 7-10 7s-7-2-10-7z"/>
          <circle cx="12" cy="10" r="3"/>
          <line x1="3" y1="1" x2="21" y2="19"/>
        </svg>
        <span class="email">jordanfitlog@mail.com</span>
        <span>&nbsp;(not shared)</span>
        <span class="switch">Switch accounts</span>
        <svg class="cloud" width="20" height="16" viewBox="0 0 24 18" fill="none" stroke="#5f6368" stroke-width="2">
          <path d="M6 16h12a4 4 0 0 0 0-8 6 6 0 0 0-11.5-1.5A4.8 4.8 0 0 0 6 16z"/>
        </svg>
      </div>
      <p class="required-note">*Required</p>
    </section>

    <section class="card question-card">
      <p class="question-label">Complete name: <span class="star">*</span></p>
      <p class="answer-line">Your answer</p>
    </section>

    <section class="card question-card">
      <p class="question-label">Email: <span class="star">*</span></p>
      <p class="answer-line">Your answer</p>
    </section>

    <section class="card question-card">
      <p class="question-label">Contact Number: <span class="star">*</span></p>
      <p class="answer-line">Your answer</p>
    </section>
  </main>

  <svg class="report-icon" width="18" height="18" viewBox="0 0 18 18">
    <path d="M2 1h14a1 1 0 0 1 1 1v11a1 1 0 0 1-1 1H5l-4 3V2a1 1 0 0 1 1-1z" fill="#5f6368"/>
    <rect x="8" y="4" width="2" height="5" fill="#fff"/>
    <rect x="8" y="10" width="2" height="2" fill="#fff"/>
  </svg>

  <div class="edit-button">
    <svg width="18" height="18" viewBox="0 0 18 18" fill="none" stroke="#5f6368" stroke-width="1.8">
      <path d="M2 16l1-4L12.5 2.5l3 3L6 15z"/>
      <line x1="10.5" y1="4.5" x2="13.5" y2="7.5"/>
    </svg>
  </div>
</body>
</html>
```